we are a college and require a design of a printable graduation certificate

our courses range from certicate III to Diploma

We would a high quality design, similar to a unveristy degree, so its meaning full to the students and looks great on the wall

our college website is: www.marlowinstitute.example.au

Industry/Entity Type

College

Requirements
Must have
• security feature like water mark or stamp

```html
<!DOCTYPE html>
<html lang="en">
<head>
<meta charset="utf-8">
<title>Graduation Certificate – Marlow Institute</title>
<link rel="stylesheet" href="https://fonts.googleapis.com/css2?family=Crimson+Text:ital,wght@0,400;0,600;0,700;1,400;1,600;1,700&display=swap">
<style>
  :root {
    --page: #ffffff;
    --paper: #eef4f8;
    --paper-deep: #dde8f0;
    --border-dark: #3f5878;
    --border-mid: #6f86a4;
    --border-light: #b9c7d8;
    --frame: #5b7394;
    --title: #8ca3b2;
    --name: #4b6b7c;
    --ink: #1f2630;
    --ribbon-pink: rgba(226, 120, 150, 0.22);
    --ribbon-gold: rgba(236, 205, 120, 0.22);
    --watermark-band: rgba(150, 150, 160, 0.16);
    --watermark-text: rgba(110, 105, 110, 0.28);
  }
  * { margin: 0; padding: 0; box-sizing: border-box; }
  html, body { width: 1200px; height: 1000px; overflow: hidden; background: var(--page); }
  body { position: relative; font-family: "Crimson Text", Georgia, serif; color: var(--ink); }

  .certificate { position: absolute; left: 30px; top: 143px; width: 1138px; height: 708px; background: var(--paper); }

  .ornamental-border {
    position: absolute; left: 25px; top: 12px; width: 1090px; height: 684px;
    border-radius: 40px;
    background:
      radial-gradient(circle at 50% 50%, var(--border-light) 0 20%, transparent 60%),
      linear-gradient(135deg, var(--border-dark), var(--border-mid) 50%, var(--border-dark));
  }

  .frame-art { position: absolute; left: 0; top: 0; }

  .inner-panel {
    position: absolute; left: 140px; top: 127px; width: 860px; height: 450px;
    background: linear-gradient(180deg, #f3f7fa, var(--paper-deep) 60%, #f1f5f8);
  }
  .ribbon-pattern {
    position: absolute; left: 140px; top: 140px; width: 860px; height: 420px;
    background:
      radial-gradient(ellipse 35% 25% at 18% 70%, var(--ribbon-pink), transparent 70%),
      radial-gradient(ellipse 30% 22% at 80% 25%, var(--ribbon-pink), transparent 70%),
      radial-gradient(ellipse 25% 30% at 30% 20%, var(--ribbon-gold), transparent 70%),
      radial-gradient(ellipse 28% 20% at 72% 60%, var(--ribbon-gold), transparent 70%);
  }

  .security-watermark {
    position: absolute; left: 210px; top: 312px; width: 735px; height: 120px;
    background: var(--watermark-band);
    overflow: hidden; text-align: center;
    font-size: 112px; font-weight: 700; line-height: 140px;
    color: var(--watermark-text); letter-spacing: 4px;
  }

  .emblem { position: absolute; left: 530px; top: 82px; width: 80px; text-align: center; }
  .emblem-circle { width: 40px; height: 40px; margin: 0 auto; border-radius: 50%; background: var(--title); }
  .emblem-name { display: block; margin-top: 4px; font-size: 11px; color: var(--name); white-space: nowrap; }

  .meta { position: absolute; font-style: italic; font-size: 14px; line-height: 19px; white-space: nowrap; }
  .meta-issue { left: 175px; top: 174px; }
  .meta-certify { left: 175px; top: 225px; }
  .meta-record { left: 753px; top: 174px; }
  .meta-record .value { font-style: normal; margin-left: 8px; }

  .award-title {
    position: absolute; left: 0; width: 1138px; top: 221px; text-align: center;
    font-size: 51px; line-height: 64px; font-weight: 400; color: var(--title);
  }
  .graduate-name {
    position: absolute; left: 0; width: 1138px; top: 267px; text-align: center;
    font-size: 65px; line-height: 80px; font-style: italic; font-weight: 600; color: var(--name);
  }
  .statement {
    position: absolute; left: 171px; top: 370px;
    font-size: 13.3px; font-style: italic; line-height: 18px; white-space: nowrap;
  }
  .statement-strong {
    position: absolute; left: 171px; top: 444px;
    font-size: 15px; font-style: italic; font-weight: 700; white-space: nowrap;
  }

  .signatory { position: absolute; top: 495px; }
  .signatory-name { font-size: 33px; font-style: italic; color: var(--name); line-height: 1; white-space: nowrap; }
  .signatory-role { font-size: 13.5px; margin-top: 8px; white-space: nowrap; }
  .signatory-dean { left: 215px; }
  .signatory-vice { right: 214px; text-align: right; }
</style>
</head>
<body>
  <main class="certificate">
    <div class="ornamental-border" role="img" aria-label="Blue guilloche ornamental border of interlocking rosettes"></div>

    <svg class="frame-art" width="1138" height="708" viewBox="0 0 1138 708" aria-hidden="true">
      <rect x="96" y="90" width="946" height="515" fill="var(--paper)" stroke="var(--frame)" stroke-width="6"/>
      <rect x="108" y="100" width="922" height="495" fill="none" stroke="var(--border-light)" stroke-width="4"/>
      <rect x="124" y="116" width="890" height="463" fill="none" stroke="var(--frame)" stroke-width="1.5"/>
      <path d="M380 118 Q569 40 758 118" fill="var(--paper)" stroke="var(--frame)" stroke-width="4"/>
      <path d="M395 126 Q569 58 743 126" fill="none" stroke="var(--border-light)" stroke-width="2"/>
      <rect x="96" y="90" width="28" height="28" fill="var(--border-light)" stroke="var(--frame)" stroke-width="2"/>
      <rect x="1014" y="90" width="28" height="28" fill="var(--border-light)" stroke="var(--frame)" stroke-width="2"/>
      <rect x="96" y="577" width="28" height="28" fill="var(--border-light)" stroke="var(--frame)" stroke-width="2"/>
      <rect x="1014" y="577" width="28" height="28" fill="var(--border-light)" stroke="var(--frame)" stroke-width="2"/>
    </svg>

    <div class="inner-panel"></div>
    <div class="ribbon-pattern" role="img" aria-label="Soft pink and gold guilloche ribbon security pattern"></div>
    <div class="security-watermark" aria-label="Security watermark">Watermark</div>

    <div class="emblem">
      <div class="emblem-circle"></div>
      <span class="emblem-name">Marlow Institute</span>
    </div>

    <p class="meta meta-issue">Then under our hand in this day<br>December 6, 2013</p>
    <p class="meta meta-certify">This to certify that</p>
    <p class="meta meta-record">Certificate number <span class="value">01564</span><br>Date of Expiration <span class="value">December 31,2013</span></p>

    <h1 class="award-title">Bachelors of Management</h1>
    <h2 class="graduate-name">John Smith Doe</h2>

    <p class="statement">Lorem ipsum dolor sit amet, consectetur adipisicing elit, sed do eiusmod tempor incididunt ut labore et dolore magna aliqua. Ut enim ad minim veniam,<br>quis nostrud exercitation ullamco laboris nisi ut aliquip ex ea commodo consequat. Duis aute irure dolor in reprehenderit in voluptate velit esse cillum dolore eu<br>fugiat nulla pariatur. Excepteur sint occaecat cupidatat non proident, sunt in culpa qui officia deserunt mollit anim id est laborum.</p>
    <p class="statement-strong">Sed ut perspiciatis unde omnis iste natus error sit voluptatem accusantium doloremque laudantium.</p>

    <div class="signatory signatory-dean">
      <p class="signatory-name">Alan Carter</p>
      <p class="signatory-role">Dean, University</p>
    </div>
    <div class="signatory signatory-vice">
      <p class="signatory-name">Clara Bennett</p>
      <p class="signatory-role">Vice Dean, University</p>
    </div>
  </main>
</body>
</html>
```